Design an investor pitch deck for Brindlecart.io

We delivered a killer investor pitch to a group of investors last week and have been asked for a deck. we need to follow up with a killer printed version. I have produced the attached file using free images from vistaloom. Feel free to change the imagery as you see fit. Check out brindlecart.io to get a feel for the look and feel we have right now.

Target Market(s)

Investors

Industry/Entity Type

Software

Font styles to use
Sans Serif
Other font styles liked:
• Helvetica

Requirements
Must have
• A new version of each of the pages in the example documents. Needs to be slick and professional
Nice to have
• Other layouts in case I add further slides
Should not have
• Childish or dated shapes or designs

```html
<!DOCTYPE html>
<html lang="en">
<head>
<meta charset="utf-8">
<title>Brindlecart.io — Investor Deck</title>
<link rel="stylesheet" href="https://fonts.googleapis.com/css2?family=Arimo:wght@400;700&display=swap">
<style>
:root{
  --navy:#1f3476;
  --orange:#f3ad2d;
  --page:#c8cbd0;
  --white:#ffffff;
  --ink:#3d3f44;
  --muted:#8a8d93;
  --rule:#d6d8dc;
  --sky:#2aa7e4;
  --deep:#1a2b5e;
}
*{box-sizing:border-box;margin:0;padding:0}
html,body{width:1200px;height:2161px;overflow:hidden}
body{background:var(--page);font-family:"Arimo",Helvetica,Arial,sans-serif;color:var(--ink);position:relative}
.slide{position:absolute;width:576px;height:324px;background:var(--white);overflow:hidden;box-shadow:0 1px 3px rgba(0,0,0,.18)}
.abs{position:absolute}
.slide-title{position:absolute;left:26px;top:22px;font-size:21px;font-weight:700;color:var(--navy)}
.slide-title .hl{color:var(--orange)}
.brand{position:absolute;left:24px;bottom:10px;display:flex;align-items:center;gap:6px;font-size:17px;font-weight:700;color:var(--navy)}
.brand .dot{width:13px;height:13px;border-radius:50%;background:var(--navy)}
.page-no{position:absolute;right:20px;bottom:12px;font-size:9px;font-weight:700;color:var(--navy)}
.caption{font-size:10px;line-height:1.35;color:var(--muted);text-align:center}
.circle{border-radius:50%;display:flex;align-items:center;justify-content:center}
/* title */
.cover-band{left:0;top:0;width:576px;height:100px;background:var(--white)}
.cover-brand{right:26px;top:30px;display:flex;align-items:center;gap:9px;font-size:36px;font-weight:700;color:var(--navy)}
.cover-brand .dot{width:28px;height:28px;border-radius:50%;background:var(--navy)}
.cover-photo{left:0;top:100px;width:576px;height:224px;background:linear-gradient(100deg,#3b3c40 0%,#56575b 55%,#6d6b66 80%,#4a4a4c 100%)}
.cover-head{left:30px;top:124px;font-size:18px;line-height:1.5;font-weight:700;color:var(--white)}
.cover-credit{left:30px;top:280px;font-size:6.5px;line-height:1.35;color:#e4e4e4}
/* big idea */
.idea-copy{left:27px;top:70px;width:310px;font-size:8.6px;line-height:1.45;text-align:justify;color:var(--ink)}
.idea-copy p{margin-bottom:8px}
.idea-panel{left:353px;top:0;width:223px;height:324px;background:var(--navy)}
.idea-panel .circle{position:absolute;left:86px;top:84px;width:58px;height:58px;background:var(--orange)}
.idea-panel p{position:absolute;left:24px;top:154px;width:175px;text-align:center;color:var(--white);font-size:12px;font-weight:700;line-height:1.45}
/* why now */
.why-col{position:absolute;top:80px;width:170px;text-align:center}
.why-col h3{font-size:12px;font-weight:700;line-height:1.3;height:34px}
.why-col .circle{width:58px;height:58px;margin:4px auto 0}
.logo-box{width:136px;height:66px;margin:18px auto 0;border:3px solid #a4a7ad;display:flex;align-items:center;justify-content:center;gap:8px}
.badge{background:#c9ccd1;border-radius:3px}
/* solution */
.sol-item{position:absolute;top:60px;width:125px;text-align:center}
.sol-visual{height:150px;display:flex;align-items:flex-end;justify-content:center;margin-bottom:10px}
/* market */
.stat{position:absolute;left:24px;display:flex;gap:12px;align-items:center;width:210px}
.stat .circle{width:38px;height:38px;flex:none;background:var(--orange)}
.stat p{font-size:9px;line-height:1.4;color:var(--muted)}
.stat b{color:var(--orange);font-size:12px}
/* business model */
.bm-cell{position:absolute;width:240px;height:100px;background:var(--navy);color:var(--white);font-size:13px;font-weight:700;line-height:1.35;text-align:center;display:flex;align-items:center;justify-content:center;padding:0 55px}
/* go to market */
.gtm-band{left:0;top:58px;width:576px;height:64px;background:var(--navy);color:var(--white);font-size:8.6px;line-height:1.45;padding:8px 26px}
.gtm-lead{left:0;top:133px;width:576px;text-align:center;color:var(--orange);font-size:12px;font-weight:700}
.gtm-line{left:26px;top:153px;width:524px;height:2px;background:var(--orange)}
.gtm-col{position:absolute;top:160px;width:160px;text-align:center;font-size:8.6px;line-height:1.4;color:var(--ink)}
.gtm-col .tri{width:0;height:0;margin:0 auto 6px;border-left:7px solid transparent;border-right:7px solid transparent;border-top:9px solid var(--orange)}
/* team */
.team-cell{position:absolute;top:84px;width:123px;height:148px;background:var(--orange);color:var(--white);font-size:11px;line-height:1.35;text-align:center;display:flex;align-items:center;justify-content:center;padding:0 10px 28px}
/* finance */
.fin-col{position:absolute;top:102px;width:150px;text-align:center}
.fin-col h3{font-size:21px;font-weight:700;color:var(--orange)}
.fin-col p{font-size:10px;color:var(--muted);margin-top:16px}
.fin-col .circle{width:38px;height:38px;margin:26px auto 0;background:var(--orange)}
/* growth */
.grow-col{position:absolute;top:120px;width:110px;text-align:center;font-size:12px;font-weight:700;line-height:1.3}
.grow-col .circle{width:58px;height:58px;margin:0 auto 10px}
/* summary */
.sum-list{position:absolute;left:30px;top:96px;width:430px;list-style:none}
.sum-list li{font-size:13.5px;line-height:1.4;color:var(--ink);margin-bottom:6px;padding-left:26px;position:relative}
.sum-list li::before{content:"";position:absolute;left:3px;top:8px;width:5px;height:5px;border-radius:50%;background:var(--orange)}
.sum-list em{font-style:normal;color:var(--orange);font-weight:700}
</style>
</head>
<body>

<!-- 1 Cover -->
<section class="slide" style="left:305px;top:20px">
  <div class="abs cover-band"></div>
  <div class="abs cover-brand"><span class="dot"></span>Brindlecart</div>
  <div class="abs cover-photo" role="img" aria-label="Photograph of a man on a sofa checking delivery status on a tablet"></div>
  <div class="abs cover-head">Waiting sucks.<br>Brindlecart makes it better.</div>
  <div class="abs cover-credit">Martin Ellery |<br>Founder @ Routewise Engineering |<br>martin@brindlecart.io</div>
</section>

<!-- 2 Big idea -->
<section class="slide" style="left:17px;top:361px">
  <h2 class="slide-title"><span class="hl">The</span> Big Idea in 125 words</h2>
  <div class="abs idea-copy">
    <p>You could track your pizza in realtime since 2015. Now business that still make people wait without a live tracking link are giving an unnecessarily poor customer experience and their brand suffers greatly.</p>
    <p>Why doesn't everyone send tracking links now? Why can't we track important things like emergency services or mission-critical business deliveries? Legacy processes, complex last-mile arrangements through multiple providers, lack of a cheap and easy solution.</p>
    <p>Brindlecart is the cleanest, simplest way to give customers a tracking link, while giving managers, drivers and developers the best possible tools to provide a great last-mile service cheaply and easily while promoting and reinforcing their brand and getting customer feedback.</p>
  </div>
  <div class="abs idea-panel">
    <div class="circle">
      <svg width="32" height="24" viewBox="0 0 32 24" fill="#fff"><rect x="1" y="3" width="18" height="13" rx="1"/><path d="M20 7h6l5 5v4H20z"/><circle cx="7" cy="19" r="3.2"/><circle cx="25" cy="19" r="3.2"/></svg>
    </div>
    <p>Waiting sucks.<br>Live tracking makes waiting for deliveries and services less painful. Brindlecart makes it easy.</p>
  </div>
  <div class="brand"><span class="dot"></span>Brindlecart</div>
</section>

<!-- 3 Why now -->
<section class="slide" style="left:606px;top:361px">
  <h2 class="slide-title">Why Now?</h2>
  <div class="why-col" style="left:10px">
    <h3 style="color:var(--orange)">Simple Global<br>Deployment</h3>
    <div class="circle" style="background:var(--orange)"><svg width="30" height="30" viewBox="0 0 30 30" fill="none" stroke="#fff" stroke-width="2"><circle cx="15" cy="15" r="12"/><ellipse cx="15" cy="15" rx="5" ry="12"/><path d="M3 15h24M5 9h20M5 21h20"/></svg></div>
    <div class="logo-box"><span class="badge" style="width:48px;height:22px"></span><span class="badge" style="width:32px;height:14px"></span></div>
  </div>
  <div class="why-col" style="left:203px">
    <h3 style="color:var(--navy)">Success of best-in-<br>class integration</h3>
    <div class="circle" style="background:var(--navy)"><svg width="26" height="32" viewBox="0 0 26 32" fill="#fff"><path d="M6 0h5l2 8 2-8h5l-4 12h-6z"/><circle cx="13" cy="21" r="9"/></svg></div>
    <div class="logo-box"><span class="badge circle" style="width:22px;height:22px"></span><span class="badge" style="width:40px;height:16px"></span><span class="badge" style="width:40px;height:14px"></span></div>
  </div>
  <div class="why-col" style="left:396px">
    <h3 style="color:var(--orange)">Shifting Customer<br>Expectation</h3>
    <div class="circle" style="background:var(--orange)"><svg width="32" height="22" viewBox="0 0 32 22" fill="#fff"><path d="M0 6l7-5 8 4 5-3 12 6-4 4-10 9-4-3-8-6z"/></svg></div>
    <div class="logo-box"><span class="badge" style="width:26px;height:32px"></span><span class="badge" style="width:30px;height:28px"></span><span class="badge" style="width:26px;height:26px"></span></div>
  </div>
  <div class="brand"><span class="dot"></span>Brindlecart</div>
  <div class="page-no">3</div>
</section>

<!-- 4 Solution -->
<section class="slide" style="left:17px;top:703px">
  <h2 class="slide-title">The Solution</h2>
  <div class="sol-item" style="left:12px">
    <div class="sol-visual">
      <svg width="96" height="70" viewBox="0 0 96 70" fill="none" stroke="var(--navy)" stroke-width="3.5" stroke-linejoin="round"><path d="M22 64h52a18 18 0 0 0 2-36 24 24 0 0 0-46-6 20 20 0 0 0-8 42z"/><circle cx="36" cy="40" r="5"/><circle cx="58" cy="28" r="5"/><circle cx="60" cy="52" r="5"/><path d="M40 38l14-8M40 43l15 7"/></svg>
    </div>
    <p class="caption">Integrations with common sources of jobs and automation tools like Linkrelay</p>
  </div>
  <div class="sol-item" style="left:152px">
    <div class="sol-visual"><div role="img" aria-label="Laptop showing the web portal with a live map" style="width:122px;height:84px;background:linear-gradient(#dfe2e6,#b9bdc3);border-radius:4px 4px 2px 2px"></div></div>
    <p class="caption">Simple web portal for keeping track of staff and jobs in realtime</p>
  </div>
  <div class="sol-item" style="left:292px">
    <div class="sol-visual"><div role="img" aria-label="Phone showing the driver app job list" style="width:70px;height:146px;background:linear-gradient(#eef0f3,#cfd3d8);border:2px solid #c2c5ca;border-radius:10px"></div></div>
    <p class="caption">A clean, intuitive driver app with 1 click to deliver the tracking link</p>
  </div>
  <div class="sol-item" style="left:432px">
    <div class="sol-visual"><div role="img" aria-label="Phone showing the customer tracking map" style="width:70px;height:146px;background:linear-gradient(#eef0f3,#cfd3d8);border:2px solid #c2c5ca;border-radius:10px"></div></div>
    <p class="caption">A customer tracking link, sent via SMS and opened with 1 click</p>
  </div>
  <div class="brand"><span class="dot"></span>Brindlecart</div>
  <div class="page-no">4</div>
</section>

<!-- 5 Market size -->
<section class="slide" style="left:606px;top:703px">
  <h2 class="slide-title">Market Size</h2>
  <div class="stat" style="top:64px"><div class="circle"><svg width="20" height="16" viewBox="0 0 20 16" fill="#fff"><rect x="0" y="2" width="11" height="9"/><path d="M12 5h4l4 4v2h-8z"/><circle cx="4" cy="13" r="2.3"/><circle cx="15" cy="13" r="2.3"/></svg></div><p><b>1.35 billion</b> annual deliveries from ecommerce by 2020 in UK</p></div>
  <div class="stat" style="top:116px"><div class="circle"><svg width="20" height="20" viewBox="0 0 20 20" fill="none" stroke="#fff" stroke-width="2"><circle cx="10" cy="10" r="8"/><path d="M2 10h16M10 2c-4 5-4 11 0 16M10 2c4 5 4 11 0 16"/></svg></div><p>Global e-commerce deliveries expected to exceed <b>24 billion</b>*</p></div>
  <div class="stat" style="top:168px"><div class="circle"><svg width="20" height="18" viewBox="0 0 20 18" fill="#fff"><rect x="1" y="9" width="4" height="9"/><rect x="8" y="4" width="4" height="14"/><rect x="15" y="0" width="4" height="18"/></svg></div><p>Based on our bulk discount effective rate of USD12c per job total market will be <b>USD2.8bn</b> in 2018</p></div>
  <p class="abs" style="left:24px;top:222px;font-size:5.5px;color:var(--muted)">*assuming UK 3.5% of world deliveries (in line with GDP %)</p>
  <svg class="abs" style="left:260px;top:52px" width="300" height="200" viewBox="0 0 300 200">
    <text x="0" y="6" font-size="5.5" fill="var(--sky)" font-family="Arimo,sans-serif">Total number of deliveries (m) generated by online orders by product type</text>
    <line x1="0" y1="170" x2="290" y2="170" stroke="#bbb" stroke-width=".6"/>
    <g fill="var(--deep)">
      <rect x="6" y="22" width="9" height="148"/><rect x="28" y="28" width="9" height="142"/><rect x="50" y="53" width="9" height="117"/><rect x="72" y="62" width="9" height="108"/><rect x="94" y="68" width="9" height="102"/><rect x="116" y="80" width="9" height="90"/><rect x="138" y="103" width="9" height="67"/><rect x="160" y="120" width="9" height="50"/><rect x="182" y="132" width="9" height="38"/><rect x="204" y="137" width="9" height="33"/><rect x="226" y="137" width="9" height="33"/><rect x="248" y="140" width="9" height="30"/>
    </g>
    <g fill="var(--sky)">
      <rect x="15" y="55" width="9" height="115"/><rect x="37" y="60" width="9" height="110"/><rect x="59" y="75" width="9" height="95"/><rect x="81" y="85" width="9" height="85"/><rect x="103" y="88" width="9" height="82"/><rect x="125" y="98" width="9" height="72"/><rect x="147" y="117" width="9" height="53"/><rect x="169" y="132" width="9" height="38"/><rect x="191" y="142" width="9" height="28"/><rect x="213" y="146" width="9" height="24"/><rect x="235" y="146" width="9" height="24"/><rect x="257" y="150" width="9" height="20"/>
    </g>
    <g fill="var(--navy)" font-size="4.6" font-family="Arimo,sans-serif" text-anchor="middle">
      <text x="15" y="182">Clothing</text><text x="37" y="182">Music</text><text x="59" y="182">Food</text><text x="81" y="182">Books</text><text x="103" y="182">Health</text><text x="125" y="182">Electricals</text><text x="147" y="182">Other</text><text x="169" y="182">Home</text><text x="191" y="182">Toys</text><text x="213" y="182">DIY</text><text x="235" y="182">Garden</text><text x="257" y="182">Sport</text>
    </g>
    <rect x="230" y="80" width="6" height="4" fill="var(--sky)"/><text x="239" y="84" font-size="4.5" fill="var(--navy)" font-family="Arimo,sans-serif">2013</text>
    <rect x="255" y="80" width="6" height="4" fill="var(--deep)"/><text x="264" y="84" font-size="4.5" fill="var(--navy)" font-family="Arimo,sans-serif">2018</text>
    <text x="0" y="196" font-size="5" fill="var(--navy)" text-decoration="underline" font-family="Arimo,sans-serif">research.ledgerline.co.uk/last-mile-report.pdf</text>
  </svg>
  <div class="brand"><span class="dot"></span>Brindlecart</div>
  <div class="page-no">5</div>
</section>

<!-- 6 Business model -->
<section class="slide" style="left:17px;top:1045px">
  <h2 class="slide-title">Business Model</h2>
  <div class="bm-cell" style="left:44px;top:70px">Transactional pricing</div>
  <div class="bm-cell" style="left:292px;top:70px">Brindlecart:<br>19c per task<br>(USD)</div>
  <div class="bm-cell" style="left:44px;top:174px">Credit and top up like a pre-paid phone card</div>
  <div class="bm-cell" style="left:292px;top:174px">Bonus credit for higher top up amounts</div>
  <div class="abs circle" style="left:227px;top:120px;width:122px;height:122px;background:var(--white)"><div class="circle" style="width:110px;height:110px;background:var(--orange)"><svg width="46" height="48" viewBox="0 0 46 48" fill="#fff"><circle cx="23" cy="10" r="9"/><rect x="4" y="30" width="8" height="18"/><rect x="15" y="24" width="8" height="24"/><rect x="26" y="28" width="8" height="20"/><rect x="37" y="22" width="8" height="26"/></svg></div></div>
  <div class="brand"><span class="dot"></span>Brindlecart</div>
  <div class="page-no">6</div>
</section>

<!-- 7 Go to market -->
<section class="slide" style="left:606px;top:1045px">
  <h2 class="slide-title">Go to Market</h2>
  <div class="abs gtm-band">Brindlecart has recently achieved market fit, with 8 paying SME customers in 4 countries. A pilot project is also in progress with a major WA Insurer. Brindlecart is a naturally viral product, with our customers sending an effective demonstration of Brindlecart to their customers. Multiple of our paying users are customers of other customers.</div>
  <div class="abs gtm-lead">Our go-to-market plan now is to establish a repeatable sales process:</div>
  <div class="abs gtm-line"></div>
  <div class="gtm-col" style="left:16px"><div class="tri"></div>Target specific geographic regions to maximise network effect, starting with Australia, Singapore and London</div>
  <div class="gtm-col" style="left:208px"><div class="tri"></div>Establish a revised automated online funnel targeting customers similar to those for whom we have demonstrated that Brindlecart solves a problem worth paying for</div>
  <div class="gtm-col" style="left:400px"><div class="tri"></div>Target medium-large firms in market segments where there is an existing pilot or where interest has been expressed by stakeholders including retail, mining, insurance repairs and healthcare through a multi-channel sales mix</div>
  <div class="brand"><span class="dot"></span>Brindlecart</div>
  <div class="page-no">7</div>
</section>

<!-- 8 Team -->
<section class="slide" style="left:17px;top:1387px">
  <h2 class="slide-title">Our Team</h2>
  <div class="team-cell" style="left:28px">Unique access to technical talent pipeline from our partnership with and colocation at WBU</div>
  <div class="team-cell" style="left:155px">Battle hardened from bootstrapping for 3 years</div>
  <div class="team-cell" style="left:282px">All key players have skin in the game</div>
  <div class="team-cell" style="left:409px">Founder &amp; board's commercial experience</div>
  <div class="abs circle" style="left:238px;top:190px;width:100px;height:100px;background:var(--white)"><div class="circle" role="img" aria-label="Team icon" style="width:88px;height:88px;background:var(--navy)"></div></div>
  <div class="brand"><span class="dot"></span>Brindlecart</div>
  <div class="page-no">8</div>
</section>

<!-- 9 Finance -->
<section class="slide" style="left:606px;top:1387px">
  <h2 class="slide-title">Finance &amp; Opportunity</h2>
  <svg class="abs" style="left:26px;top:130px" width="506" height="12" viewBox="0 0 506 12"><line x1="0" y1="6" x2="496" y2="6" stroke="#b8bbc0" stroke-width="2"/><path d="M494 1l10 5-10 5z" fill="#b8bbc0"/></svg>
  <div class="fin-col" style="left:10px"><h3>2016</h3><p>$250k 'FFF'</p><div class="circle"><svg width="18" height="14" viewBox="0 0 18 14" fill="none" stroke="#fff" stroke-width="2.6"><path d="M2 7l5 5 9-10"/></svg></div></div>
  <div class="fin-col" style="left:160px"><h3>Now</h3><p>Deal details</p><div class="circle"></div></div>
  <div class="fin-col" style="left:324px"><h3>6-8 months</h3><p>Planned raise</p><div class="circle"></div></div>
  <div class="brand"><span class="dot"></span>Brindlecart</div>
  <div class="page-no">9</div>
</section>

<!-- 10 Growth -->
<section class="slide" style="left:17px;top:1728px">
  <h2 class="slide-title">How to Fuel Growth</h2>
  <div class="grow-col" style="left:40px;color:var(--orange)"><div class="circle" style="background:var(--orange)"><svg width="28" height="28" viewBox="0 0 28 28" fill="#fff"><path d="M14 2l12 12h-7v12h-10v-12h-7z"/></svg></div>Ramp up<br>UX efforts</div>
  <div class="grow-col" style="left:162px;color:var(--navy)"><div class="circle" style="background:var(--navy)"><svg width="30" height="22" viewBox="0 0 30 22" fill="#fff"><path d="M2 12l26-8-2 5-10 4 -4 8-2-6-8 0z"/></svg></div>Customer<br>journey<br>management</div>
  <div class="grow-col" style="left:284px;color:var(--orange)"><div class="circle" style="background:var(--orange)"><svg width="30" height="30" viewBox="0 0 30 30" fill="#fff" stroke="#fff" stroke-width="1.6"><circle cx="15" cy="15" r="5"/><circle cx="5" cy="5" r="3"/><circle cx="25" cy="5" r="3"/><circle cx="5" cy="25" r="3"/><circle cx="25" cy="25" r="3"/><path d="M5 5l20 20M25 5L5 25"/></svg></div>Digital<br>marketing<br>expertise</div>
  <div class="grow-col" style="left:406px;color:var(--navy)"><div class="circle" style="background:var(--navy)"><svg width="18" height="30" viewBox="0 0 18 30" fill="none" stroke="#fff" stroke-width="2.4"><rect x="2" y="2" width="14" height="26" rx="2"/><path d="M7 24h4"/></svg></div>Activation<br>of digital<br>campaign</div>
  <div class="brand"><span class="dot"></span>Brindlecart</div>
  <div class="page-no">10</div>
</section>

<!-- 11 Summary -->
<section class="slide" style="left:606px;top:1728px">
  <h2 class="slide-title">Summary</h2>
  <div class="abs circle" style="left:400px;top:30px;width:126px;height:126px;background:var(--navy)">
    <svg width="58" height="70" viewBox="0 0 58 70" fill="none" stroke="#fff" stroke-width="3"><rect x="4" y="8" width="40" height="54" rx="3"/><rect x="15" y="3" width="18" height="9" rx="2" fill="#fff"/><path d="M12 24h4M22 24h14M12 34h4M22 34h14M12 44h4M22 44h10"/><circle cx="44" cy="54" r="11" fill="var(--navy)"/><path d="M38 54l4 4 8-8"/></svg>
  </div>
  <ul class="sum-list">
    <li>A <em>clear problem</em> for a big market</li>
    <li>The right <em>people</em> and a great <em>pipeline of talent</em></li>
    <li>Great <em>technology foundation</em> and <em>technical skills</em></li>
    <li>Paying customers in <em>multiple countries</em></li>
    <li>A clear opportunity for <em>capital</em> to create and drive the <em>growth engine</em></li>
  </ul>
  <div class="brand"><span class="dot"></span>Brindlecart</div>
  <div class="page-no">11</div>
</section>

</body>
</html>
```